Hedge fund needs power point design for marketing pitch

We need a designer to make our power point pitch more aesthetically appealing to potential clients. We will be marketing our hedge fund to high net worth individuals and financial institutions. The ideal design will look professional and project confidence to our potential clients. We have attached a rough outline of what we have completed so far. We have also attached example cover pages for 2 pitch books produced by our competitors.

Target Market(s)

Financial institutions and wealthy investors

Industry/Entity Type

Finance

Requirements
Must have
• must use our logo and current slides. Must look professional

```html
<!DOCTYPE html>
<html lang="en">
<head>
<meta charset="utf-8">
<title>Halvorsen Derivatives Fund LP – Pitch Deck</title>
<link href="https://fonts.googleapis.com/css2?family=Cinzel:wght@400;600&family=Open+Sans:wght@400;600;700&display=swap" rel="stylesheet">
<style>
:root{
  --navy:#1b2b48;
  --navy-deep:#0f1b31;
  --gold:#c9a227;
  --gold-light:#f1dd8a;
  --gold-dark:#9c7a12;
  --olive:#4a4418;
  --green:#1f3a22;
  --ink:#2e2e2e;
  --muted:#555;
  --red:#d0312d;
  --white:#fff;
}
*{margin:0;padding:0;box-sizing:border-box}
html,body{width:1200px;height:702px;overflow:hidden}
body{
  background:radial-gradient(ellipse at 50% 40%,#27406a 0%,var(--navy) 45%,var(--navy-deep) 100%);
  font-family:"Open Sans",Arial,sans-serif;color:var(--ink);position:relative;
}
.slide{position:absolute;width:264px;height:198px;background:var(--white);overflow:hidden;box-shadow:0 2px 6px rgba(0,0,0,.45)}
.slide-head{
  height:17px;background:linear-gradient(180deg,var(--gold-light) 0%,var(--gold) 55%,var(--gold-dark) 100%);
  border-bottom:1px solid #fff;box-shadow:0 1px 0 #d9c57a;
  font-family:"Cinzel",serif;font-size:8px;font-weight:600;letter-spacing:.4px;color:#3b3418;
  padding:4px 0 0 8px;text-transform:uppercase;
}
.slide-foot{position:absolute;left:0;bottom:0;width:264px;height:30px}
.slide-foot .url{position:absolute;left:38px;bottom:5px;font-size:5.6px;font-weight:700;letter-spacing:1.3px;color:#222}
.slide-body{position:absolute;left:8px;top:24px;right:8px;font-size:5.4px;line-height:1.55}
.pt{position:relative;padding-left:9px;margin-bottom:5px}
.pt::before{content:"";position:absolute;left:1px;top:2px;border-left:4px solid var(--gold);border-top:2px solid transparent;border-bottom:2px solid transparent}
.sub{position:relative;padding-left:15px;margin-bottom:3px;color:var(--muted)}
.sub::before{content:"";position:absolute;left:8px;top:2.2px;width:2.4px;height:2.4px;border-radius:50%;background:var(--gold)}
.visual{position:absolute;border:1px solid #bbb}

/* cover */
.cover-band{position:absolute;left:0;top:0;width:100%;height:62px;background:linear-gradient(180deg,var(--gold) 0%,var(--gold-light) 55%,#fff 100%)}
.brand{position:absolute;left:0;right:0;top:48px;text-align:center}
.brand-name{font-family:"Cinzel",serif;font-size:18px;font-weight:600;letter-spacing:1px;color:#1c1c1c}
.brand-sub{font-family:"Cinzel",serif;font-size:8px;color:var(--gold-dark);letter-spacing:.6px;margin-top:1px}
.cover-title{position:absolute;left:0;right:0;top:116px;text-align:center;font-family:"Cinzel",serif}
.cover-title .fund{font-size:9.5px;color:#222;letter-spacing:.6px}
.cover-title .conf{font-size:9px;color:var(--gold);letter-spacing:1px;margin-top:3px}

/* simulated performance */
.sim-sub{position:absolute;left:8px;top:22px;font-size:5.6px;font-weight:600}
.sim-chart{position:absolute;left:8px;top:32px;width:100px;height:66px}
.sim-notes{position:absolute;left:106px;top:32px;right:6px;font-size:3.6px;line-height:1.5;color:var(--muted)}
.sim-notes div{position:relative;padding-left:5px;margin-bottom:4.2px}
.sim-notes div::before{content:"";position:absolute;left:0;top:1.4px;width:2px;height:2px;border-radius:50%;background:var(--gold)}
.sim-table{position:absolute;left:6px;top:104px;width:252px;border-collapse:collapse;font-size:3.4px}
.sim-table th,.sim-table td{text-align:right;padding:0 1px;line-height:1.35}
.sim-table th:first-child,.sim-table td:first-child{text-align:left}
.sim-table thead tr:last-child th{border-bottom:.6px solid #333}
.sim-table .neg{color:var(--red)}
.sim-cap{position:absolute;left:6px;right:6px;top:140px;font-size:3.4px;line-height:1.4;color:#333}
.sim-cap b{font-weight:700}

/* risk diagram slide */
.risk-body{right:142px;line-height:1.75}
.risk-body .pt{margin-bottom:6px}
.risk-note{position:absolute;left:17px;top:168px;font-size:5.4px}
.risk-cycle{position:absolute;left:138px;top:36px}

/* why invest */
.why-body .sub{margin-bottom:4.5px}
.why-body .narrow{margin-right:86px}
.why-visual{position:absolute;left:176px;top:112px;width:74px;height:54px;background:radial-gradient(ellipse at 50% 45%,#7fb23a 0%,#b7c77a 35%,#e8dcaa 60%,#fff 78%)}

/* risk table */
.terms{position:absolute;left:7px;top:23px;width:250px}
.terms-row{display:flex;gap:4px;margin-bottom:1.4px}
.terms-row span{height:9.4px;font-size:4.4px;line-height:9.4px;color:#fff;padding-left:3px}
.terms-row .k{width:122px;background:var(--gold)}
.terms-row .v{flex:1;background:var(--green)}

/* thank you */
.thanks{background:linear-gradient(160deg,#6e6e6e 0%,#4a4a4a 55%,#3a3a3a 100%)}
.thanks .brand{top:42px}
.thanks .brand-name,.thanks .brand-sub{color:#fff}
.thanks-big{position:absolute;left:0;right:0;top:92px;text-align:center;font-family:"Cinzel",serif;color:#fff}
.thanks-big .t1{font-size:21px;font-weight:600;letter-spacing:.5px}
.thanks-big .t2{font-size:10px;letter-spacing:1px}
.contact{position:absolute;left:0;right:0;top:147px;text-align:center;color:#fff;font-size:6px;line-height:1.85}
.contact svg{vertical-align:-1px;margin-right:2px}
</style>
</head>
<body>

<svg width="0" height="0" style="position:absolute" aria-hidden="true">
  <defs>
    <linearGradient id="goldWave" x1="0" x2="1">
      <stop offset="0" stop-color="#e9d37a"/><stop offset=".5" stop-color="#c9a227"/><stop offset="1" stop-color="#9c7a12"/>
    </linearGradient>
    <symbol id="footWave" viewBox="0 0 264 30">
      <path d="M0 10 C80 0 170 20 264 3 L264 30 L0 30Z" fill="url(#goldWave)"/>
      <path d="M0 15 C90 7 170 23 264 9 L264 30 L0 30Z" fill="#4a4418"/>
      <path d="M0 18 C90 11 170 26 264 13 L264 27 L0 27Z" fill="#fff"/>
      <rect x="0" y="27" width="264" height="3" fill="url(#goldWave)"/>
    </symbol>
  </defs>
</svg>

<!-- Cover -->
<section class="slide" style="left:34px;top:28px">
  <div class="cover-band"></div>
  <div class="brand">
    <div class="brand-name">HALVORSEN</div>
    <div class="brand-sub">CAPITAL MANAGEMENT LLC</div>
  </div>
  <div class="cover-title">
    <div class="fund">HALVORSEN DERIVATIVES FUND LP</div>
    <div class="conf">CONFIDENTIAL</div>
  </div>
  <div class="slide-foot"><svg width="264" height="30"><use href="#footWave"/></svg><span class="url">www.halvorsencap.com</span></div>
</section>

<!-- Investment Objective -->
<section class="slide" style="left:319px;top:28px">
  <div class="slide-head">Investment Objective</div>
  <div class="slide-body">
    <div class="pt">Profit from inefficiencies in equity and index options markets</div>
    <div class="sub">Buy options that are underpriced</div>
    <div class="sub">Sell options that are overpriced</div>
    <div class="pt" style="margin-top:6px">Achieve outsized and consistent returns by maintaining a small and nimble fund that can exploit price inefficiencies and move in and out of trades quickly</div>
  </div>
  <div class="visual" role="img" aria-label="Photo of seedlings growing from stacks of gold coins" style="left:9px;top:96px;width:244px;height:76px;background:linear-gradient(180deg,#e7e2d4 0%,#9a8a5a 45%,#4a3a22 100%)"></div>
  <div class="slide-foot"><svg width="264" height="30"><use href="#footWave"/></svg><span class="url">www.halvorsencap.com</span></div>
</section>

<!-- Investment Strategy -->
<section class="slide" style="left:610px;top:28px">
  <div class="slide-head">Investment Strategy</div>
  <div class="slide-body" style="right:86px">
    <div class="pt">Strategy derived from a dynamic optimization problem that maximizes returns within a given risk constraint.</div>
    <div class="pt">Parameters / assumptions</div>
    <div class="sub">Assume liquid markets</div>
    <div class="sub">Assume a price discount/premium on each trade (5-10%)</div>
    <div class="pt" style="margin-top:4px">Solution - the optimization problem tells us:</div>
    <div class="sub">When to buy or sell contracts</div>
    <div class="sub">Which contracts to buy or sell</div>
    <div class="sub">How many contracts to buy or sell</div>
    <div class="pt" style="margin-top:4px">We make trades based on these solutions while hitting the price discount/premium offered by the market.</div>
  </div>
  <svg style="position:absolute;left:150px;top:96px" width="112" height="78" viewBox="0 0 112 78" aria-label="Strategy risk versus return chart">
    <line x1="6" y1="72" x2="6" y2="2" stroke="#555" stroke-width=".6"/>
    <line x1="6" y1="72" x2="108" y2="72" stroke="#555" stroke-width=".6"/>
    <polygon points="6,0 4.5,3 7.5,3" fill="#555"/><polygon points="110,72 107,70.5 107,73.5" fill="#555"/>
    <text x="8" y="5" font-size="2.8" fill="#777">HIGHER</text>
    <text x="7" y="70" font-size="2.8" fill="#777">LOWER</text>
    <text x="98" y="70" font-size="2.8" fill="#777">HIGHER</text>
    <text x="2" y="60" font-size="2.4" fill="#777" transform="rotate(-90 2 60)">EXPECTED RISK</text>
    <text x="50" y="76.5" font-size="2.4" fill="#777">EXPECTED RETURN</text>
    <g fill="#9a8a28" stroke="#e6d98e" stroke-width="1.2">
      <circle cx="24" cy="58" r="8"/><circle cx="45" cy="45" r="8"/><circle cx="63" cy="34" r="8"/><circle cx="82" cy="22" r="8"/><circle cx="100" cy="10" r="8"/>
    </g>
    <g fill="#fff" font-size="2.7" text-anchor="middle">
      <text x="24" y="58">Cash</text><text x="24" y="61">Strategy</text>
      <text x="45" y="45">Cautious</text><text x="45" y="48">Strategy</text>
      <text x="63" y="34">Neutral</text><text x="63" y="37">Strategy</text>
      <text x="82" y="22">Balanced</text><text x="82" y="25">Strategy</text>
      <text x="100" y="10">Growth</text><text x="100" y="13">Strategy</text>
    </g>
  </svg>
  <div class="slide-foot"><svg width="264" height="30"><use href="#footWave"/></svg><span class="url">www.halvorsencap.com</span></div>
</section>

<!-- Simulated Performance 8% -->
<section class="slide" style="left:899px;top:28px">
  <div class="slide-head">Simulated Performance</div>
  <div class="sim-sub">Under Our Average Price Discount/premium (8%)</div>
  <svg class="sim-chart" viewBox="0 0 100 66" aria-label="Distribution of simulated returns">
    <line x1="6" y1="2" x2="6" y2="52" stroke="#444" stroke-width=".5"/>
    <line x1="6" y1="52" x2="98" y2="52" stroke="#444" stroke-width=".5"/>
    <path d="M6 52 C10 50 12 4 17 4 C22 4 26 40 40 50 L98 51.5" fill="none" stroke="#333" stroke-width=".5"/>
    <path d="M6 52 C12 50 16 16 24 16 C32 16 40 44 60 50 L98 51.5" fill="none" stroke="#888" stroke-width=".5"/>
    <path d="M6 52 C16 51 24 28 36 28 C48 28 60 46 98 51" fill="none" stroke="#bbb" stroke-width=".5"/>
    <rect x="30" y="58" width="30" height="6" fill="none" stroke="#999" stroke-width=".3"/>
    <text x="32" y="61.5" font-size="2.3" fill="#555">monthly · quarterly · annual</text>
  </svg>
  <div class="sim-notes">
    <div>Mean simulated annual return is 302%</div>
    <div>Only 1% of simulated annual returns are lower than 25.7%</div>
    <div>The mean 3-year and 5-year simulated returns are 6,109% and 96,093%</div>
    <div>The worst simulated 3-year return out of 10,000 simulated observations is +88%</div>
    <div>The worst simulated 5-year return out of 10,000 simulated observations is +1,048%</div>
  </div>
  <table class="sim-table">
    <thead>
      <tr><th></th><th></th><th colspan="7" style="text-align:center">Percentiles</th><th></th><th></th><th></th></tr>
      <tr><th>period</th><th>mean</th><th>1%</th><th>10%</th><th>25%</th><th>50%</th><th>75%</th><th>90%</th><th>99%</th><th>min</th><th>max</th><th>% +</th></tr>
    </thead>
    <tbody>
      <tr><td>monthly</td><td class="neg">13.3</td><td>(13.0)</td><td>(5.7)</td><td>0.2</td><td class="neg">8.6</td><td>19.4</td><td>31.6</td><td>58.5</td><td>(19.3)</td><td>118.8</td><td class="neg">76%</td></tr>
      <tr><td>quarterly</td><td class="neg">37.4</td><td>(15.5)</td><td>1.2</td><td>13.8</td><td class="neg">31.8</td><td>55.1</td><td>80.5</td><td>137.7</td><td>(28.5)</td><td>292.2</td><td class="neg">91%</td></tr>
      <tr><td>1 year</td><td class="neg">302.0</td><td>25.7</td><td>96.1</td><td>155.1</td><td class="neg">251.8</td><td>394.1</td><td>563.2</td><td>1,040.7</td><td class="neg">(27.7)</td><td>2,251.7</td><td class="neg">99.8%</td></tr>
      <tr><td>3 year</td><td class="neg">6,109.1</td><td>634.2</td><td>1,511.5</td><td>2,455.8</td><td class="neg">4,291.1</td><td>7,576.9</td><td>12,373.8</td><td>31,693.1</td><td class="neg">88.4</td><td>85,014.2</td><td class="neg">100%</td></tr>
      <tr><td>5 year</td><td class="neg">96,093.4</td><td>5,128.6</td><td>14,450.8</td><td>27,087.3</td><td class="neg">54,222.7</td><td>112,032.5</td><td>212,569.1</td><td>660,578.3</td><td class="neg">1,047.8</td><td>2,173,490.8</td><td class="neg">100%</td></tr>
    </tbody>
  </table>
  <p class="sim-cap">Assumes 8% price discount per trade and liquid markets. The table shows returns expressed as a percentage of the initial investment, by the amount of time since the investment period began. Each row shows estimated returns distributions using Monte Carlo simulation and bootstrapping methods. The estimates are drawn from simulated samples containing 10,000 observations for each term. <b>The simulated returns do not account for fees and taxes, which may reduce an investor's actual returns.</b></p>
  <div class="slide-foot"><svg width="264" height="30"><use href="#footWave"/></svg><span class="url">www.halvorsencap.com</span></div>
</section>

<!-- Simulated Performance 5% -->
<section class="slide" style="left:32px;top:248px">
  <div class="slide-head">Simulated Performance</div>
  <div class="sim-sub">Under A More Conservative Assumed Price Discount/premium (5%)</div>
  <svg class="sim-chart" viewBox="0 0 100 66" aria-label="Distribution of simulated returns">
    <line x1="6" y1="2" x2="6" y2="52" stroke="#444" stroke-width=".5"/>
    <line x1="6" y1="52" x2="98" y2="52" stroke="#444" stroke-width=".5"/>
    <path d="M6 52 C10 50 12 4 17 4 C22 4 26 40 40 50 L98 51.5" fill="none" stroke="#333" stroke-width=".5"/>
    <path d="M6 52 C12 50 16 16 24 16 C32 16 40 44 60 50 L98 51.5" fill="none" stroke="#888" stroke-width=".5"/>
    <path d="M6 52 C16 51 24 28 36 28 C48 28 60 46 98 51" fill="none" stroke="#bbb" stroke-width=".5"/>
    <rect x="30" y="58" width="30" height="6" fill="none" stroke="#999" stroke-width=".3"/>
    <text x="32" y="61.5" font-size="2.3" fill="#555">monthly · quarterly · annual</text>
  </svg>
  <div class="sim-notes">
    <div>Mean simulated annual return is 129%</div>
    <div>1% of the time, annual simulated returns are lower than -29.5%</div>
    <div>The mean 3-year and 5-year simulated returns are 1,129% and 6,759%</div>
    <div>Only 1% of 5-year returns fall below +216%</div>
    <div>The worst simulated 5-year return out of 10,000 simulated observations is -16%</div>
  </div>
  <table class="sim-table">
    <thead>
      <tr><th></th><th></th><th colspan="7" style="text-align:center">Percentiles</th><th></th><th></th><th></th></tr>
      <tr><th>period</th><th>mean</th><th>1%</th><th>10%</th><th>25%</th><th>50%</th><th>75%</th><th>90%</th><th>99%</th><th>min</th><th>max</th><th>% +</th></tr>
    </thead>
    <tbody>
      <tr><td>monthly</td><td>6.7</td><td>(17.4)</td><td>(10.0)</td><td>(4.0)</td><td>4.3</td><td>15.1</td><td>26.2</td><td>51.8</td><td>(22.7)</td><td>100.0</td><td>63%</td></tr>
      <tr><td>quarterly</td><td class="neg">21.6</td><td>(25.7)</td><td>(10.9)</td><td>0.6</td><td class="neg">16.9</td><td>37.1</td><td>59.9</td><td>114.1</td><td>(37.8)</td><td>200.8</td><td class="neg">76%</td></tr>
      <tr><td>1 year</td><td class="neg">129.2</td><td>(29.5)</td><td>12.2</td><td>46.7</td><td class="neg">100.3</td><td>178.0</td><td>280.4</td><td>555.1</td><td>(62.1)</td><td>1,403.4</td><td class="neg">94%</td></tr>
      <tr><td>3 year</td><td class="neg">1,129.3</td><td>37.3</td><td>198.8</td><td>390.7</td><td class="neg">750.0</td><td>1,406.6</td><td>2,436.3</td><td>6,122.8</td><td>(67.0)</td><td>23,804.0</td><td class="neg">99.7%</td></tr>
      <tr><td>5 year</td><td class="neg">6,759.0</td><td>216.5</td><td>816.4</td><td>1,636.4</td><td class="neg">3,523.6</td><td>7,368.2</td><td>14,846.8</td><td>52,779.2</td><td>(15.9)</td><td>260,998.9</td><td class="neg">99.9%</td></tr>
    </tbody>
  </table>
  <p class="sim-cap">Assumes 5% price discount per trade and liquid markets. The table shows returns expressed as a percentage of the initial investment, by the amount of time since the investment period began. Each row shows estimated returns distributions using Monte Carlo simulation and bootstrapping methods. The estimates are drawn from simulated samples containing 10,000 observations for each term. <b>The simulated returns do not account for fees and taxes, which may reduce an investor's actual returns.</b></p>
  <div class="slide-foot"><svg width="264" height="30"><use href="#footWave"/></svg><span class="url">www.halvorsencap.com</span></div>
</section>

<!-- Actual Performance -->
<section class="slide" style="left:319px;top:248px">
  <div class="slide-head">Actual Performance</div>
  <div class="slide-body">
    <div class="pt">The fund will launch in May 2016.</div>
    <div class="pt">We will report fund performance on a monthly basis starting in June.</div>
  </div>
  <div class="visual" role="img" aria-label="Illustration of a business figure silhouette in front of blue market charts" style="left:9px;top:62px;width:244px;height:107px;background:linear-gradient(180deg,#2a62b8 0%,#5d9be0 55%,#cfe3f7 100%)"></div>
  <div class="slide-foot"><svg width="264" height="30"><use href="#footWave"/></svg><span class="url">www.halvorsencap.com</span></div>
</section>

<!-- Risk Management diagram -->
<section class="slide" style="left:610px;top:248px">
  <div class="slide-head">Risk Management</div>
  <div class="slide-body risk-body">
    <div class="pt">Our top priority is safety</div>
    <div class="pt">If the market does not offer a price discount or premium, we trade at the best available price to stay within our trading parameters.</div>
    <div class="pt">This approach minimizes losses in illiquid markets.</div>
    <div class="pt">The simulated strategy performance at substantially lower average price discount/premium, relative to the average we have achieved to date, exhibits limited downside risk</div>
  </div>
  <div class="risk-note">(see simulation results at 5% versus 8% discount/premium)</div>
  <svg class="risk-cycle" width="118" height="122" viewBox="0 0 130 135" aria-label="Risk management process cycle">
    <circle cx="65" cy="66" r="42" fill="none" stroke="#333" stroke-width="1.6"/>
    <text x="65" y="66" text-anchor="middle" font-family="Open Sans,Arial,sans-serif" font-weight="700" font-size="15" fill="#2a2a2a">RISK</text>
    <text x="65" y="73" text-anchor="middle" font-family="Open Sans,Arial,sans-serif" font-size="4.3" fill="#2a2a2a">MANAGEMENT</text>
    <text x="65" y="80" text-anchor="middle" font-family="Open Sans,Arial,sans-serif" font-weight="700" font-size="6" fill="#2a2a2a">PROCESS</text>
    <g font-family="Open Sans,Arial,sans-serif" font-size="3.8" font-weight="700" text-anchor="middle" fill="#222">
      <circle cx="65" cy="24" r="15" fill="#fff" stroke="#333" stroke-width="2.2"/>
      <text x="65" y="23">ASSESS</text><text x="65" y="27.5">RISK</text>
      <circle cx="65" cy="108" r="15" fill="#fff" stroke="#333" stroke-width="2.2"/>
      <text x="65" y="107">REVIEW</text><text x="65" y="111.5">CONTROLS</text>
      <circle cx="23" cy="66" r="15" fill="#fff" stroke="#c9a227" stroke-width="2.2"/>
      <text x="23" y="65">IDENTIFY</text><text x="23" y="69.5">RISK</text>
      <circle cx="107" cy="66" r="15" fill="#fff" stroke="#c9a227" stroke-width="2.2"/>
      <text x="107" y="65">CONTROL</text><text x="107" y="69.5">RISK</text>
    </g>
  </svg>
  <div class="slide-foot"><svg width="264" height="30"><use href="#footWave"/></svg><span class="url">www.halvorsencap.com</span></div>
</section>

<!-- Risk Management terms -->
<section class="slide" style="left:896px;top:248px">
  <div class="slide-head">Risk Management</div>
  <div class="terms">
    <div class="terms-row"><span class="k">Fund</span><span class="v">Halvorsen Derivatives Fund LP</span></div>
    <div class="terms-row"><span class="k">Management Company</span><span class="v">Halvorsen Capital Management LLC</span></div>
    <div class="terms-row"><span class="k">Eligible Investors</span><span class="v">Qualified Clients</span></div>
    <div class="terms-row"><span class="k">Minimum Initial Investment</span><span class="v">$50,000</span></div>
    <div class="terms-row"><span class="k">Additional Contributions</span><span class="v">Monthly on 1st of month; min $10,000</span></div>
    <div class="terms-row"><span class="k">Redemptions</span><span class="v">Monthly with 10 day notice</span></div>
    <div class="terms-row"><span class="k">Lock-up period</span><span class="v">none</span></div>
    <div class="terms-row"><span class="k">Management Fee</span><span class="v">2%</span></div>
    <div class="terms-row"><span class="k">Performance Fee</span><span class="v">20%</span></div>
    <div class="terms-row"><span class="k">Legal Counsel</span><span class="v">Marlow Pryce LLP</span></div>
    <div class="terms-row"><span class="k">Administrator</span><span class="v">Ridgeway Fund Services LLC</span></div>
    <div class="terms-row"><span class="k">Auditor</span><span class="v">To be determined</span></div>
    <div class="terms-row"><span class="k">Prime Broker</span><span class="v">Northgate Brokerage LLC</span></div>
  </div>
  <div class="slide-foot"><svg width="264" height="30"><use href="#footWave"/></svg><span class="url">www.halvorsencap.com</span></div>
</section>

<!-- Why Invest -->
<section class="slide" style="left:319px;top:470px">
  <div class="slide-head">Why Invest?</div>
  <div class="slide-body why-body">
    <div class="pt">Halvorsen Derivatives Fund, LP offers:</div>
    <div class="sub">A large return potential</div>
    <div class="sub">Low risk over a 3 to 5 year horizon</div>
    <div class="sub">High liquidity (monthly withdrawals with no lockup period – subject to gate policy???)</div>
    <div class="sub">A Low minimum investment</div>
    <div class="sub">Transparent investment return properties</div>
    <div class="sub narrow">Returns that do not correlate highly with returns in the stock and bond markets. The added diversification offered the fund reduces an investor's overall portfolio risk</div>
    <div class="sub narrow">Partnership in a small, agile fund that can generate returns that larger less nimble, competitors cannot</div>
  </div>
  <div class="why-visual" role="img" aria-label="Illustration of a green seedling growing from a pile of gold coins"></div>
  <div class="slide-foot"><svg width="264" height="30"><use href="#footWave"/></svg><span class="url">www.halvorsencap.com</span></div>
</section>

<!-- Thank you -->
<section class="slide thanks" style="left:606px;top:470px" role="img" aria-label="Closing slide over a grey photo of a hand using a tablet">
  <div class="brand">
    <div class="brand-name">HALVORSEN</div>
    <div class="brand-sub">CAPITAL MANAGEMENT LLC</div>
  </div>
  <div class="thanks-big">
    <div class="t1">THANK YOU!</div>
    <div class="t2">FOR WATCHING!</div>
  </div>
  <div class="contact">
    <div><svg width="6" height="6" viewBox="0 0 10 10"><circle cx="5" cy="5" r="4.3" fill="none" stroke="#fff" stroke-width="1"/><path d="M3.3 2.8l1 1-.6.8c.4.8 1 1.4 1.8 1.8l.8-.6 1 1-.7.9C4.8 7.5 2.6 5.3 2.4 3.4z" fill="#fff"/></svg>555-014-2290</div>
    <div><svg width="6" height="5" viewBox="0 0 10 8"><rect x=".5" y=".5" width="9" height="7" fill="none" stroke="#fff"/><path d="M.5.5L5 4.5 9.5.5" fill="none" stroke="#fff"/></svg>sales@halvorsencap.com</div>
    <div><svg width="5" height="6" viewBox="0 0 8 10"><path d="M4 0a3.6 3.6 0 0 0-3.6 3.6C.4 6.3 4 10 4 10s3.6-3.7 3.6-6.4A3.6 3.6 0 0 0 4 0z" fill="#fff"/><circle cx="4" cy="3.6" r="1.3" fill="#555"/></svg>Street Name, City Name Zipcode-012345</div>
  </div>
  <div class="slide-foot"><svg width="264" height="30"><use href="#footWave"/></svg><span class="url" style="color:#fff;left:34px">www.halvorsencap.com</span></div>
</section>

</body>
</html>
```